Business Card Design Project

Construction

Industry/Entity Type

Business

Contact Information for Business Card

I've had the same logo for about 5 years. The logo itself is fine, however I'm looking to get a new design on the card. The green for the log is fine but the grey for the rest of the card is kind of dark and blah. Would like a new look. I'll send the file with the logo.

```html
<!DOCTYPE html>
<html lang="en">
<head>
<meta charset="utf-8">
<title>Keystone Ridge Commercial Builders – Business Card</title>
<link href="https://fonts.googleapis.com/css2?family=Roboto:ital,wght@0,400;0,500;0,700;0,900;1,400&family=Roboto+Condensed:wght@700&display=swap" rel="stylesheet">
<style>
  :root{
    --page:#3a3b3c;
    --card:#2a2b2c;
    --card-shade:#323334;
    --green:#3fae5a;
    --green-light:#8fd49c;
    --green-dark:#1f7a36;
    --silver-1:#f4f4f4;
    --silver-2:#b9bbbd;
    --white:#ffffff;
    --ink:#1e1e1e;
  }
  *{box-sizing:border-box;margin:0;padding:0}
  html,body{width:799px;height:1200px;overflow:hidden}
  body{background:var(--page);font-family:"Roboto",sans-serif;color:var(--white);position:relative}
  .card{position:absolute;left:50px;width:700px;height:400px;border-radius:26px;background:
      linear-gradient(135deg,var(--card) 0%,var(--card-shade) 55%,var(--card) 100%);overflow:hidden;
      box-shadow:0 14px 30px rgba(0,0,0,.45)}
  .card--front{top:130px}
  .card--back{top:670px}

  .headline{position:absolute;text-transform:uppercase;line-height:1}
  .headline__main{display:block;font-family:"Roboto Condensed",sans-serif;font-weight:700;font-size:50px;letter-spacing:1px}
  .headline__sub{display:block;font-family:"Roboto Condensed",sans-serif;font-weight:700;font-size:24px;letter-spacing:1px;margin-top:4px}

  .brand-mark{position:absolute;display:flex;align-items:center;gap:8px;font-weight:700;font-size:15px;color:var(--green);text-transform:uppercase;letter-spacing:.5px}
  .brand-mark__square{width:22px;height:22px;background:var(--green)}

  /* front */
  .license-band{position:absolute;left:0;top:150px;width:700px;height:78px;
      background:linear-gradient(180deg,var(--silver-1),var(--silver-2));color:var(--ink);padding:10px 26px}
  .license-band p{font-size:17px;line-height:26px}
  .license-band strong{font-weight:700}
  .license-tag{position:absolute;right:0;top:208px;height:40px;padding:0 28px 0 40px;background:linear-gradient(90deg,var(--green-dark),var(--green));
      clip-path:polygon(22px 0,100% 0,100% 100%,0 100%);display:flex;align-items:center;font-weight:700;font-size:17px;letter-spacing:.5px}
  .naics{position:absolute;left:26px;top:248px;width:440px;font-size:17px;line-height:23px}
  .naics strong{font-weight:700}
  .assurance{position:absolute;left:0;top:318px;width:410px;height:40px;background:linear-gradient(90deg,var(--green-light),var(--green));
      clip-path:polygon(0 0,calc(100% - 26px) 0,100% 100%,0 100%);display:flex;align-items:center;padding-left:26px;font-size:16px;letter-spacing:1px;text-transform:uppercase}
  .silver-foot{position:absolute;left:0;bottom:0;width:700px;height:20px;background:linear-gradient(90deg,var(--silver-2),var(--silver-1))}
  .cert-seals{position:absolute;right:40px;top:265px;display:flex;gap:18px}

  /* back */
  .license-note{position:absolute;left:30px;top:82px;font-size:16px;letter-spacing:.5px}
  .contact-block{position:absolute;left:310px;top:180px}
  .contact-block__name{font-size:27px;font-weight:500;color:var(--green-light)}
  .contact-block__title{font-size:17px;margin-top:2px}
  .contact-list{list-style:none;margin-top:12px}
  .contact-list li{display:flex;align-items:center;gap:12px;font-size:17px;line-height:25px}
  .contact-list svg{width:15px;height:15px;fill:var(--green-light)}
  .years-badge{position:absolute;left:26px;top:205px;width:170px}
  .years-badge__ribbon{background:var(--green);padding:4px 12px;font-weight:900;font-size:20px;text-transform:uppercase;letter-spacing:1px;text-align:center;
      clip-path:polygon(0 0,100% 0,94% 50%,100% 100%,0 100%,6% 50%)}
  .years-badge__over{display:block;width:56px;margin:0 auto -4px;background:var(--silver-1);color:var(--ink);border-radius:28px 28px 0 0;font-size:11px;font-weight:700;text-align:center;padding-top:6px}
  .years-badge__caption{font-size:10px;text-transform:uppercase;text-align:center;margin-top:3px;letter-spacing:.5px}
  .service-band{position:absolute;right:0;bottom:0;width:480px;height:56px;background:linear-gradient(90deg,var(--green-dark),var(--green-light));
      clip-path:polygon(40px 0,100% 0,100% 100%,0 100%);display:flex;align-items:center;justify-content:center;font-size:19px}
  .silver-left{position:absolute;left:0;bottom:0;width:240px;height:56px;background:linear-gradient(180deg,var(--silver-2),var(--silver-1))}
</style>
</head>
<body>

<section class="card card--front" aria-label="Card front">
  <div class="brand-mark" style="left:26px;top:40px"><span class="brand-mark__square"></span>Keystone Ridge</div>
  <h1 class="headline" style="left:240px;top:22px">
    <span class="headline__main">Keystone Ridge</span>
    <span class="headline__sub">Commercial Builders</span>
  </h1>
  <div class="license-band">
    <p><strong>LICENSES :</strong> » A - General Engineering » B - General Building</p>
    <p>» C21 Demo/Bldg. Moving » C36 Plumbing</p>
  </div>
  <div class="license-tag">LICENSE #2047718</div>
  <p class="naics"><strong>NAICS CODES:</strong> 236220, 238110, 236118, 23810, 238350, 2389390, 327320</p>
  <div class="assurance">Licensed | Bonded | Insured</div>
  <div class="cert-seals">
    <svg width="100" height="100" viewBox="0 0 100 100" role="img" aria-label="Certification seal"><circle cx="50" cy="50" r="48" fill="#ffffff"/><circle cx="50" cy="50" r="38" fill="none" stroke="#2a2b2c" stroke-width="3"/></svg>
    <svg width="100" height="100" viewBox="0 0 100 100" role="img" aria-label="Certification seal"><circle cx="50" cy="50" r="48" fill="#ffffff"/><circle cx="50" cy="50" r="38" fill="none" stroke="#2a2b2c" stroke-width="3"/></svg>
  </div>
  <div class="silver-foot"></div>
</section>

<section class="card card--back" aria-label="Card back">
  <div class="brand-mark" style="left:30px;top:44px"><span class="brand-mark__square"></span>Keystone Ridge</div>
  <p class="license-note">LICENSE #2047718</p>
  <h2 class="headline" style="left:240px;top:34px">
    <span class="headline__main">Keystone Ridge</span>
    <span class="headline__sub">Commercial Builders</span>
  </h2>
  <div class="years-badge">
    <span class="years-badge__over">OVER</span>
    <div class="years-badge__ribbon">25 Years</div>
    <p class="years-badge__caption">of service excellence</p>
  </div>
  <div class="contact-block">
    <p class="contact-block__name">Marcus Hale, DMP</p>
    <p class="contact-block__title">President, Founder &amp; CEO</p>
    <ul class="contact-list">
      <li><svg viewBox="0 0 24 24"><path d="M6.6 10.8a15 15 0 006.6 6.6l2.2-2.2a1 1 0 011-.25 11.4 11.4 0 003.6.57 1 1 0 011 1V20a1 1 0 01-1 1A17 17 0 013 4a1 1 0 011-1h3.5a1 1 0 011 1c0 1.25.2 2.45.57 3.57a1 1 0 01-.25 1z"/></svg>(310) 555-0148</li>
      <li><svg viewBox="0 0 24 24"><path d="M2 5h20v14H2z M2 5l10 8 10-8" stroke="#2a2b2c" stroke-width="1.5"/></svg>marcus@keystoneridgebuilders.com</li>
      <li><svg viewBox="0 0 24 24"><circle cx="12" cy="12" r="10"/><path d="M2 12h20M12 2c3 3 3 17 0 20M12 2c-3 3-3 17 0 20" stroke="#2a2b2c" stroke-width="1.4" fill="none"/></svg>www.keystoneridgebuilders.com</li>
    </ul>
  </div>
  <div class="silver-left"></div>
  <div class="service-band">Serving all of Southern California</div>
</section>

</body>
</html>
```